【概要】 住宅会社様の完成見学会のバナー制作です。 Web広告で使用するためのバナーデザインを募集します。 【依頼内容】 ・サイズ: 横1200× 縦628px、横1080× 縦1080px ・作成数: 1種類 ・利用用途:SNS広告(facebook/Instagram) 【目的】 完成見学会の来場促進(ぺージは下記) https://kanerudo.co.jp/ie/news/ie-news-8412-2-2-2-2-3-2-2-2-2-2-2-2/ 【デザインイメージ】 ・ターゲット層:30代~40代前半の主婦(若め)子供ができたばかり。旦那は普通の会社員。 ・雰囲気:お任せします 【使用素材】 添付のものをお使い下さい(全て使用しなくて結構です) ※開催日ですが、11/20.21は終了しているので削除し、残りの日程をバナーに表記してください。 【参考(クライアント)サイト】 https://kanerudo.co.jp https://hanamiho.com 【契約金額(税抜)】 3,000円/デザイン 最終納品のファイル形式は、AIもしくはPSDデータとしますが、デザイン提出段階では、PDFもしくはJPEGで問題ありません。 その他ご質問等ありましたら、気軽にお問い合わせください。 ご応募をお待ちしております! |
| https://kanerudo.co.jp/ie/news/ie-news-8412-2-2-2-2-3-2-2-2-2-2-2-2/ | ||

```html
<!DOCTYPE html>
<html lang="ja">
<head>
<meta charset="utf-8">
<title>Open House Banner</title>
<link href="https://fonts.googleapis.com/css2?family=Noto+Sans+JP:wght@500;700&family=Noto+Serif+JP:wght@400;500;700&family=Playfair+Display:ital,wght@1,500;1,700&display=swap" rel="stylesheet">
<style>
  :root {
    --page: #ffffff;
    --guide: #8a8a8a;
    --brand-red: #c1272d;
    --panel-brown: #3b1d18;
    --text-light: #ffffff;
    --logo-ink: #3a3a3a;
    --sky-top: #2f7fd0;
    --sky-low: #8fc0ea;
    --wall: #3d4550;
    --ground: #d9d6d0;
  }
  html, body { margin: 0; padding: 0; overflow: hidden; }
  body {
    width: 1200px; height: 1200px;
    background: var(--page);
    position: relative;
    font-family: "Noto Sans JP", sans-serif;
  }
  .guide-line {
    position: absolute; left: 599px; top: 0;
    width: 2px; height: 1200px; background: var(--guide);
  }
  .banner {
    position: absolute; left: 0; top: 293px;
    width: 1189px; height: 620px;
    background: var(--brand-red);
    overflow: hidden;
  }
  .photo {
    position: absolute; left: 20px; top: 18px; right: 22px; bottom: 20px;
    background:
      linear-gradient(180deg, transparent 0 72%, var(--ground) 72% 100%),
      linear-gradient(90deg, transparent 0 28%, var(--wall) 28% 70%, transparent 70% 100%),
      linear-gradient(180deg, var(--sky-top) 0%, var(--sky-low) 80%);
  }
  .headline {
    position: absolute; left: 68px; top: 40px; margin: 0;
    font-family: "Playfair Display", "Noto Serif JP", serif;
    font-style: italic; font-weight: 500;
    font-size: 92px; line-height: 1.12;
    color: var(--text-light); letter-spacing: 2px;
  }
  .tagline {
    position: absolute; left: 40px; top: 295px; margin: 0;
    color: var(--text-light); font-weight: 500;
    font-size: 44px; line-height: 1.45;
    text-shadow: 0 2px 6px rgba(0,0,0,.35);
  }
  .tagline strong { font-weight: 700; font-size: 50px; }
  .brand {
    position: absolute; left: 20px; bottom: 20px;
    display: flex; align-items: center; gap: 12px;
    background: rgba(255,255,255,.85);
    padding: 12px 22px 14px 18px;
  }
  .brand-mark { width: 30px; height: 30px; background: var(--brand-red); }
  .brand-name {
    font-family: "Noto Sans JP", sans-serif; font-weight: 500;
    font-size: 36px; color: var(--logo-ink); letter-spacing: 2px;
  }
  .event-corner { position: absolute; right: 0; top: 0; width: 200px; height: 200px; }
  .schedule {
    position: absolute; left: 872px; top: 232px;
    width: 295px; height: 376px;
    background: var(--panel-brown);
    color: var(--text-light);
    font-family: "Noto Serif JP", serif; font-weight: 700;
  }
  .year {
    position: absolute; left: 22px; top: 22px; margin: 0;
    font-size: 30px; line-height: 1;
  }
  .date {
    position: absolute; left: 22px; width: 265px; height: 120px; margin: 0;
  }
  .date-first { top: 70px; }
  .date-second { top: 190px; }
  .month {
    position: absolute; left: 0; top: 0;
    font-size: 44px; line-height: 1;
  }
  .slash {
    position: absolute; left: 10px; top: 18px;
    width: 50px; height: 80px;
  }
  .days {
    position: absolute; left: 38px; top: 58px;
    font-size: 46px; line-height: 1; white-space: nowrap;
  }
  .days .dow { font-size: 20px; font-weight: 500; margin: 0 4px 0 2px; }
  .days .tilde { font-weight: 500; margin: 0 8px 0 0; }
  .hours {
    position: absolute; left: 22px; top: 318px; margin: 0;
    font-size: 40px; line-height: 1; white-space: nowrap;
  }
</style>
</head>
<body>
  <div class="guide-line"></div>

  <section class="banner">
    <div class="photo" role="img" aria-label="Photo of the finished two-storey house with dark grey siding under a blue sky"></div>

    <h1 class="headline">OPEN<br>HOUSE</h1>
    <p class="tagline">安心の<strong>定額制</strong>で建てる<br>「<strong>完全自由設計</strong>」の家</p>

    <div class="brand">
      <span class="brand-mark"></span>
      <span class="brand-name">kanerudo</span>
    </div>

    <svg class="event-corner" viewBox="0 0 200 200" aria-label="Event!">
      <polygon points="0,0 200,0 200,200" fill="var(--brand-red)"/>
      <text x="128" y="70" transform="rotate(45 128 70)" text-anchor="middle"
            fill="#ffffff" font-family="Playfair Display, serif" font-style="italic"
            font-weight="700" font-size="40">Event!</text>
    </svg>

    <div class="schedule">
      <p class="year">2021.</p>

      <div class="date date-first">
        <span class="month">11</span>
        <svg class="slash" viewBox="0 0 50 80" aria-hidden="true">
          <line x1="46" y1="2" x2="4" y2="78" stroke="#ffffff" stroke-width="3"/>
        </svg>
        <span class="days">27<span class="dow">Sat</span><span class="tilde">~</span>28<span class="dow">Sun</span></span>
      </div>

      <div class="date date-second">
        <span class="month">12</span>
        <svg class="slash" viewBox="0 0 50 80" aria-hidden="true">
          <line x1="46" y1="2" x2="4" y2="78" stroke="#ffffff" stroke-width="3"/>
        </svg>
        <span class="days">4<span class="dow">Sat</span><span class="tilde">~</span>5<span class="dow"> Sun</span></span>
      </div>

      <p class="hours">10:00~17:00</p>
    </div>
  </section>
</body>
</html>
```